Pelton|Marsh & Quillan business card contest

We need a logo for an upscale boutique diversified company involved in real estate, investments, cattle, and more. Our businesses DO NOT need to be reflected in the business card nor do we want them noted. This is our logo and colors and we love our logo and colors. Our logo looks best against a black background and we like to include the firm name in our logo usage. importantly, the names Pelton and Marsh are separated by | not / and we use an ampersand not the word and.
On the front of the card, we want to include:
company logo and name (Pelton|Marsh & Quillan)
on the back, we would definitely include:
address, email, cell #
logo and name (smaller size than front)

The variable will be location of individual name and title (mine for example is ) - whether on the front OR on the back. interested in variations from which to choose
Dr. Neil R. Whitcombe, CFA
Scientifique des Fusées Financières

we would like to use contemporary symbols for address, email address, cell # with an option for web site that we do not intend to use initially. we like two sided cards and believe this design should use four rounded corners with the standard size. we prefer thicker card stock and may look at metal.

```html
<!DOCTYPE html>
<html lang="en">
<head>
<meta charset="utf-8">
<title>Pelton|Marsh &amp; Quillan — Business Card</title>
<link rel="stylesheet" href="https://fonts.googleapis.com/css2?family=Lato:wght@400;700&display=swap">
<style>
  :root {
    --stage: #3a3b3e;
    --card-black: #0c0c0d;
    --card-white: #ffffff;
    --brand-orange: #e27a24;
    --brand-grey: #8c8c8e;
    --text-grey: #4a4a4c;
    --name-grey-dark: #58585a;
  }
  * { margin: 0; padding: 0; box-sizing: border-box; }
  html, body { width: 1200px; height: 900px; overflow: hidden; }
  body {
    background: var(--stage);
    font-family: "Lato", sans-serif;
    position: relative;
  }
  .card {
    position: absolute;
    left: 290px;
    width: 620px;
    height: 354px;
    border-radius: 34px;
  }
  .card--front { top: 48px; background: var(--card-black); }
  .card--back { top: 450px; background: var(--card-white); }

  .wordmark {
    position: absolute;
    display: flex;
    align-items: center;
    gap: 14px;
    font-weight: 400;
    white-space: nowrap;
  }
  .wordmark__square { background: var(--brand-orange); flex: none; }

  .card--front .wordmark {
    left: 50%; top: 50%;
    transform: translate(-50%, -50%);
    font-size: 40px;
    color: var(--brand-grey);
  }
  .card--front .wordmark__square { width: 34px; height: 34px; }

  .card--back .wordmark {
    right: 38px; top: 62px;
    font-size: 24px;
    color: var(--name-grey-dark);
    gap: 10px;
  }
  .card--back .wordmark__square { width: 20px; height: 20px; }

  .rule {
    position: absolute;
    left: 318px; right: 38px; top: 190px;
    height: 1.5px;
    background: var(--brand-orange);
  }
  .identity { position: absolute; left: 42px; top: 160px; }
  .identity__name {
    font-size: 27px;
    font-weight: 700;
    color: var(--brand-orange);
    line-height: 1.1;
  }
  .identity__cred { font-size: 16px; font-weight: 400; }
  .identity__title {
    font-size: 15px;
    font-weight: 700;
    color: var(--brand-grey);
    margin-top: 4px;
  }
  .contacts {
    position: absolute;
    left: 42px; top: 236px;
    list-style: none;
  }
  .contacts__item {
    display: flex;
    align-items: flex-start;
    gap: 14px;
    font-size: 15px;
    color: var(--text-grey);
    line-height: 1.25;
    margin-bottom: 9px;
  }
  .contacts__icon { width: 18px; height: 18px; flex: none; fill: var(--brand-orange); margin-top: 1px; }
</style>
</head>
<body>
  <section class="card card--front" aria-label="Card front">
    <div class="wordmark">
      <span class="wordmark__square"></span>
      <span class="wordmark__name">Pelton|Marsh &amp; Quillan</span>
    </div>
  </section>

  <section class="card card--back" aria-label="Card back">
    <div class="wordmark">
      <span class="wordmark__square"></span>
      <span class="wordmark__name">Pelton|Marsh &amp; Quillan</span>
    </div>
    <div class="rule"></div>
    <div class="identity">
      <p class="identity__name">Dr. Neil R. Whitcombe<span class="identity__cred">, CFA</span></p>
      <p class="identity__title">Scientifique des Fusées Financières</p>
    </div>
    <ul class="contacts">
      <li class="contacts__item">
        <svg class="contacts__icon" viewBox="0 0 24 24" aria-hidden="true"><path d="M6.6 10.8a15.1 15.1 0 0 0 6.6 6.6l2.2-2.2a1 1 0 0 1 1-.25 11.4 11.4 0 0 0 3.6.57 1 1 0 0 1 1 1V20a1 1 0 0 1-1 1A17 17 0 0 1 3 4a1 1 0 0 1 1-1h3.5a1 1 0 0 1 1 1c0 1.25.2 2.45.57 3.57a1 1 0 0 1-.25 1z"/></svg>
        <span>214 380 5167</span>
      </li>
      <li class="contacts__item">
        <svg class="contacts__icon" viewBox="0 0 24 24" aria-hidden="true"><path d="M2 5h20v14H2z M4 7v.5l8 5 8-5V7l-8 5z" fill-rule="evenodd"/></svg>
        <span>neil@peltonmarsh.com</span>
      </li>
      <li class="contacts__item">
        <svg class="contacts__icon" viewBox="0 0 24 24" aria-hidden="true"><path d="M12 2a7 7 0 0 0-7 7c0 5.2 7 13 7 13s7-7.8 7-13a7 7 0 0 0-7-7zm0 9.5A2.5 2.5 0 1 1 12 6.5a2.5 2.5 0 0 1 0 5z"/></svg>
        <span>4810 Larkspur Ridge Road<br>Suite 300, Fairhollow, 57219</span>
      </li>
    </ul>
  </section>
</body>
</html>
```